Birch & Ember Website Design (Rustic/Western)

OVERVIEW
Birch & Ember Supply House (aka Birch & Ember) manufactures rustic / western furniture and décor for cabins, lodges, and ranches. We also offer a line of accessories to complement our product line.
WEB PAGE (www.BirchAndEmber.example)
We are looking for a new web page design to represent our mountain-style (log furniture) and country-style (barnwood furniture) product line. We would like to re-create our existing homepage with a similar style template for our product line.
Our website is currently under construction – a draft has been published as an example outline. We are currently using Plinkora.example for our online store.
THEME
The overall theme needs to appear rustic, yet elegant. Listed below are only suggestions, not requirements. Please use your own creativity.
* Photographs: We will use our own photographs, for now any photograph will suffice.
* Background Colors: dark brown (rgb 21-9-2), medium brown (rgb 39-17-4), light brown (rgb 72-34-3). White background is also an option.
* Font Colors: beige (rgb 233-164-118), gold (rgb 151-98-2)
• Mountain-Style Images: cabin, wildlife, mountains, fishing, wildlife, trees, etc.
* Mountain-Style Colors: hunter green
* Country-Style Images: western, ranch, barn, farm animals, horse buggies, horseshoes, etc.
* Country-Style Colors: maroon
Thanks to all who are participating.
Target Market(s)
Outdoor enthusiasts who enjoy mountain living or country living. Our primary target market is our local market and within a 100 mile radius of our location.
Industry/Entity Type
Construction
Requirements
Must have
- Rustic, yet elegant design.
Homepage and product template page for displaying each item.
Nice to have
- Source code and functionality is optional.
Mountain-Style theme to represent our collection of log furniture and décor suited for cabins and lodges. Suggested color: hunter green. Images may include cabin, wildlife, mountains, fishing, wildlife, trees, etc.
Country-Style theme to represent our collection of barnwood furniture and décor suited for farms and ranches. Suggested color: maroon. Images may include western, ranch, barn, farm animals, horse buggies, horseshoes, etc.

```html
<!DOCTYPE html>
<html lang="en">
<head>
<meta charset="utf-8">
<title>Birch &amp; Ember Supply House — Rustic / Western Furniture &amp; Accessories</title>
<link rel="stylesheet" href="https://fonts.googleapis.com/css2?family=Arimo:wght@400;700&display=swap">
<style>
  :root {
    --dark-brown: #150902;
    --medium-brown: #271104;
    --light-brown: #482203;
    --footer-brown: #3d1d06;
    --beige: #e9a476;
    --gold: #976202;
    --card-frame: #d99a6c;
    --white: #ffffff;
    --black: #000000;
    --nav-text: #e8d6c6;
    --caption-bg: rgba(0, 0, 0, 0.82);
  }
  * { box-sizing: border-box; margin: 0; padding: 0; }
  html, body { width: 974px; height: 1200px; overflow: hidden; background: var(--dark-brown); }
  body { font-family: "Arimo", Arial, sans-serif; position: relative; }

  .page { position: relative; width: 974px; height: 1200px; overflow: hidden; }

  /* Hero */
  .hero { position: absolute; left: 0; top: 0; width: 974px; height: 535px; border-top: 8px solid var(--black); }
  .hero-photo {
    position: absolute; inset: 0;
    background:
      radial-gradient(ellipse 260px 150px at 700px 190px, rgba(150,140,125,0.85) 0%, rgba(110,95,80,0.55) 55%, transparent 100%),
      radial-gradient(ellipse 90px 110px at 370px 270px, rgba(245,190,90,0.75) 0%, transparent 100%),
      radial-gradient(ellipse 80px 100px at 90px 320px, rgba(240,175,80,0.6) 0%, transparent 100%),
      radial-gradient(ellipse 420px 110px at 560px 470px, rgba(160,30,25,0.85) 0%, rgba(120,25,18,0.6) 55%, transparent 100%),
      linear-gradient(180deg, #7a4416 0%, #8c5020 22%, #6e3a14 45%, #4a200e 68%, #3a140a 100%);
  }
  .hero-caption {
    position: absolute; left: 425px; top: 253px; width: 390px; height: 152px;
    background: var(--caption-bg); padding: 10px 44px 0 10px; text-align: right;
  }
  .hero-title { color: var(--white); font-weight: 700; font-size: 31px; line-height: 38px; }
  .hero-text { color: var(--white); font-size: 14px; margin-top: 12px; text-align: left; padding-left: 2px; white-space: nowrap; }
  .hero-arrows { position: absolute; right: 40px; bottom: 12px; display: flex; gap: 6px; }
  .hero-arrow { width: 20px; height: 20px; display: block; }

  /* Sidebar */
  .sidebar {
    position: absolute; left: 120px; top: 0; width: 166px; height: 455px;
    background: rgba(21, 9, 2, 0.93);
  }
  .brand {
    height: 128px; display: flex; flex-direction: column; align-items: center; justify-content: center; gap: 8px;
    background: rgba(0,0,0,0.35);
  }
  .brand-mark { width: 40px; height: 40px; border-radius: 50%; background: var(--light-brown); }
  .brand-name { color: var(--white); font-weight: 700; font-size: 15px; letter-spacing: 0.5px; }
  .side-nav { list-style: none; margin: 12px 20px 0; }
  .side-nav li {
    height: 23px; line-height: 22px; text-align: center; font-size: 10px; color: var(--nav-text);
    border-bottom: 1px dotted rgba(232, 214, 198, 0.45);
  }

  /* Content */
  .content {
    position: absolute; left: 0; top: 535px; width: 974px; height: 515px;
    background: linear-gradient(180deg, #221003 0%, var(--dark-brown) 100%);
  }
  .section-title {
    position: absolute; left: 122px; top: 33px; color: var(--beige);
    font-size: 28px; font-weight: 400; letter-spacing: 0.2px; white-space: nowrap;
  }
  .body-text { position: absolute; left: 122px; width: 730px; color: var(--beige); font-size: 11px; line-height: 18px; }
  .body-text.intro { top: 77px; }
  .body-text.outro { top: 350px; }

  .feature-card {
    position: absolute; top: 151px; width: 328px; height: 170px;
    border: 4px solid var(--card-frame); overflow: hidden;
  }
  .feature-card.cabin { left: 147px; }
  .feature-card.lodge { left: 502px; }
  .card-photo { position: absolute; inset: 0; }
  .cabin .card-photo {
    background:
      radial-gradient(ellipse 120px 60px at 140px 95px, rgba(150,70,40,0.9) 0%, transparent 100%),
      linear-gradient(180deg, #26301c 0%, #3a4a2c 30%, #6a3a22 55%, #8a4428 80%, #3a2a1a 100%);
  }
  .lodge .card-photo {
    background:
      radial-gradient(ellipse 90px 70px at 160px 70px, rgba(235,228,210,0.95) 0%, transparent 100%),
      linear-gradient(180deg, #6a4a2a 0%, #a8988a 30%, #8a7a66 60%, #2a2018 100%);
  }
  .card-caption {
    position: absolute; left: 0; right: 0; bottom: 8px; height: 38px;
    background: var(--caption-bg); color: var(--white); font-size: 20px; line-height: 38px; text-align: center;
  }

  .mountain-band {
    position: absolute; left: 128px; right: 124px; bottom: 0; height: 98px;
    background:
      radial-gradient(ellipse 200px 70px at 150px 98px, rgba(110,55,12,0.85) 0%, transparent 100%),
      radial-gradient(ellipse 230px 80px at 480px 98px, rgba(110,55,12,0.85) 0%, transparent 100%),
      linear-gradient(180deg, transparent 0%, rgba(72, 34, 3, 0.5) 50%, rgba(72, 34, 3, 0.8) 100%);
  }

  /* Footer */
  .footer {
    position: absolute; left: 0; top: 1050px; width: 974px; height: 150px;
    background: var(--footer-brown); border-top: 4px solid var(--black);
  }
  .footer-nav { position: absolute; left: 128px; top: 14px; display: flex; list-style: none; }
  .footer-nav li { font-size: 8px; color: var(--nav-text); height: 30px; line-height: 30px; padding: 0 6px; white-space: nowrap; }
  .footer-nav li.active { background: var(--black); color: var(--white); padding: 0 8px; }
  .follow { position: absolute; left: 0; right: 0; top: 60px; text-align: center; color: var(--nav-text); font-size: 9px; }
  .social { position: absolute; left: 0; right: 0; top: 77px; display: flex; justify-content: center; gap: 4px; }
  .social span { width: 22px; height: 22px; background: #6a3a14; display: block; }
  .copyright { position: absolute; left: 0; right: 0; top: 112px; text-align: center; color: var(--nav-text); font-size: 9px; line-height: 13px; }
</style>
</head>
<body>
<div class="page">

  <header class="hero">
    <div class="hero-photo" role="img" aria-label="Photograph of a log cabin living room with stone fireplace, warm lamps and a red patterned rug"></div>

    <div class="hero-caption">
      <h1 class="hero-title">Lorem ipsum dolor sit<br>amet, consectetur</h1>
      <p class="hero-text">Lorem ipsum dolor sit amet, consectetur adipisicing elit</p>
      <div class="hero-arrows">
        <svg class="hero-arrow" viewBox="0 0 20 20" aria-label="Previous slide"><path d="M12 5 L7 10 L12 15" fill="none" stroke="#fff" stroke-width="2"/></svg>
        <svg class="hero-arrow" viewBox="0 0 20 20" aria-label="Next slide"><path d="M8 5 L13 10 L8 15" fill="none" stroke="#fff" stroke-width="2"/></svg>
      </div>
    </div>
  </header>

  <nav class="sidebar">
    <div class="brand">
      <span class="brand-mark"></span>
      <span class="brand-name">Birch &amp; Ember</span>
    </div>
    <ul class="side-nav">
      <li>HOME</li>
      <li>ONLINE STORE</li>
      <li>BEDROOM</li>
      <li>KITCHEN</li>
      <li>LIVING ROOM</li>
      <li>OFFICE / BAR ROOMS</li>
      <li>OUTDOOR</li>
      <li>LIGHTING</li>
      <li>WALL DECOR</li>
      <li>ACCESSORIES</li>
      <li>ABOUT US</li>
      <li>CONTACT US</li>
    </ul>
  </nav>

  <main class="content">
    <h2 class="section-title">RUSTIC / WESTERN FURNITURE &amp; ACCESSORIES</h2>
    <p class="body-text intro">Lorem ipsum dolor sit amet, consectetur adipisicing elit, sed do eiusmod tempor incididunt ut labore et dolore magna aliqua.<br>Ut enim ad minim veniam, quis nostrud exercitation ullamco laboris nisi ut aliquip ex ea commodo consequat.</p>

    <article class="feature-card cabin">
      <div class="card-photo" role="img" aria-label="Photograph of a log cabin home among pine trees"></div>
      <div class="card-caption">Lorem ipsum dolor</div>
    </article>
    <article class="feature-card lodge">
      <div class="card-photo" role="img" aria-label="Photograph of a lodge dining room with timber beams, curtains and a chandelier"></div>
      <div class="card-caption">Lorem ipsum dolor</div>
    </article>

    <p class="body-text outro">Lorem ipsum dolor sit amet, consectetur adipisicing elit, sed do eiusmod tempor incididunt ut labore et dolore magna aliqua.<br>Ut enim ad minim veniam, quis nostrud exercitation ullamco laboris nisi ut aliquip ex ea commodo consequat.</p>

    <div class="mountain-band" role="img" aria-label="Illustration of mountain ridges, pine trees and deer in silhouette"></div>
  </main>

  <footer class="footer">
    <ul class="footer-nav">
      <li class="active">HOME</li>
      <li>ONLINE STORE</li>
      <li>BEDROOM</li>
      <li>KITCHEN</li>
      <li>LIVING ROOM OFFICE / BAR ROOM OUTDOOR</li>
      <li>LIGHTING</li>
      <li>WALL DECOR</li>
      <li>ACCESSORIES</li>
      <li>ABOUT US</li>
      <li>CONTACT US</li>
    </ul>
    <p class="follow">Follow Us</p>
    <div class="social"><span></span><span></span><span></span><span></span></div>
    <p class="copyright">© 2014 Copyright Birch &amp; Ember Supply House<br>All Rights Reserved.</p>
  </footer>

</div>
</body>
</html>
```